IT Professional business card with a hometown feel and a little edgy.

My business name is Tamble Website Solutions. But I have ended up doing much more. I live in a very small remote community, where everyone knows everyone. We like the one-on-one customer service in this community. I do computer tutoring, virus removal, networking, and software training. My clients are businesses and private individuals.

My website is tamblewebsitesolutions.example, when I first designed it I was going for a fresh, clean look, which I still like. But I am thinking about making the website a bit more edgy to match my new logo from ArtHively (logo attached). At this time my website does not display the new logo, but I plan on redesigning the website in the future to match the logo and business card.

My tag line is "let the web do the work for you"

I'm thinking I would like to have the business card printed with a metallic finish.
Updates

Please do not use black backgrounds, or any solid dark colors. Prefer light or white backgrounds.

Target Market(s)

Small businesses. Individuals that need computer help at home.

Industry/Entity Type

It Company

Contact Information for Business Card

Nora Prandell
Tamble Website Solutions
PO Box 7153
Alder Bay, WA 98422
Cell: 555-271-3096
nora@tamblewebsitesolutions.example
tamblewebsitesolutions.example

Font styles to use
Serif

Requirements
Must have
• Must have all the information listed in "Business Card Details"
• Must use the logo provided.
• Use the colors from the provided logo
Nice to have
• Would like to use my tagline "let the web do the work for you" all lowercase

```html
<!DOCTYPE html>
<html lang="en">
<head>
<meta charset="utf-8">
<title>Tamble Website Solutions – Business Card</title>
<link rel="stylesheet" href="https://fonts.googleapis.com/css2?family=Red+Hat+Display:wght@500;600;700&display=swap">
<style>
  :root {
    --page: #ffffff;
    --ink: #1d1d1d;
    --brand-green: #2f6b35;
    --card-edge: #4a4a4a;
    --back-top: #d8e4cf;
    --back-mid: #a3c88f;
    --back-bottom: #77ae5f;
    --silver: #f4f4f4;
  }
  * { margin: 0; padding: 0; box-sizing: border-box; }
  html, body {
    width: 960px; height: 1200px; overflow: hidden;
    background: var(--page);
    font-family: "Red Hat Display", Arial, sans-serif;
    color: var(--ink);
  }
  .canvas { position: relative; width: 960px; height: 1200px; }

  .card {
    position: absolute; left: 70px; width: 820px; height: 462px;
    border-radius: 32px;
  }
  .card--front { top: 110px; background: #fff; border: 1px solid var(--card-edge); }
  .card--back {
    top: 627px;
    background: linear-gradient(180deg, var(--back-top) 0%, var(--back-mid) 55%, var(--back-bottom) 100%);
  }

  .holder-name {
    position: absolute; left: 54px; top: 145px;
    font-size: 29px; font-weight: 600; letter-spacing: -0.2px;
  }

  .brand {
    position: absolute; display: flex; align-items: center; gap: 22px;
    font-weight: 600;
  }
  .brand__square { display: block; flex: none; }
  .brand__name { line-height: 1.0; }
  .card--front .brand { left: 620px; top: 86px; color: var(--brand-green); font-size: 26px; }
  .card--front .brand__square { width: 26px; height: 26px; background: var(--brand-green); }
  .card--back .brand { left: 440px; top: 183px; color: var(--silver); font-size: 32px; }
  .card--back .brand__square { width: 34px; height: 34px; background: var(--silver); }

  .contact {
    position: absolute; top: 326px;
    font-size: 18px; font-weight: 700; line-height: 29.5px;
    list-style: none;
  }
  .contact--personal { left: 54px; }
  .contact--company { left: 515px; }
  .contact__company-name { color: var(--brand-green); }

  .tagline {
    position: absolute; left: 0; right: 0; top: 375px;
    text-align: center; color: #fff;
    font-size: 24px; font-weight: 700; letter-spacing: 3px;
  }
</style>
</head>
<body>
<main class="canvas">
  <section class="card card--front" aria-label="Card front">
    <h1 class="holder-name">Nora Prandell</h1>
    <div class="brand">
      <span class="brand__square"></span>
      <span class="brand__name">Tamble<br>Website<br>Solutions</span>
    </div>
    <ul class="contact contact--personal">
      <li>Cell: 555-271-3096</li>
      <li>nora@tamblewebsitesolutions.example</li>
      <li>tamblewebsitesolutions.example</li>
    </ul>
    <ul class="contact contact--company">
      <li class="contact__company-name">Tamble Website Solutions</li>
      <li>PO Box 7153</li>
      <li>Alder Bay, WA 98422</li>
    </ul>
  </section>

  <section class="card card--back" aria-label="Card back">
    <div class="brand">
      <span class="brand__square"></span>
      <span class="brand__name">Tamble<br>Website<br>Solutions</span>
    </div>
    <p class="tagline">let the web do the work for you</p>
  </section>
</main>
</body>
</html>
```